Our new beauty salon requires a price list brochure

Our beauty clinic is a medical grade skin care clinic. So our salon is very clinical and professional in appearance. I would like the colours to be similar to our logo design with some nice texture or abstract shapes thrown in.
Pricelist, contact details and logo is attached
I would prefer it to be a 3 fold brochure.

Target Market(s)

Females aged 30-50

Colors
85acd3
cedeed
c4c4c4
5c5c5c
000000
ffffff
eea3c7
f9d9e8
dbdbdb

Requirements
Must have
• easy to read

```html
<!DOCTYPE html>
<html lang="en">
<head>
<meta charset="utf-8">
<title>Willow Aesthetics – Price List</title>
<link href="https://fonts.googleapis.com/css2?family=Lato:wght@300;400;700&display=swap" rel="stylesheet">
<style>
  :root {
    --slate: #566473;
    --band-grey: #9d9ba6;
    --blush: #f9d9e8;
    --blush-pale: #fdeef1;
    --blush-strip: #f7d3da;
    --text-dark: #4a4d55;
    --rule: #7a8290;
    --white: #ffffff;
  }
  * { margin: 0; padding: 0; box-sizing: border-box; }
  html, body { width: 1200px; height: 848px; overflow: hidden; }
  body { font-family: "Lato", sans-serif; color: var(--text-dark); background: var(--white); }

  .brochure {
    position: relative; width: 1200px; height: 848px; overflow: hidden;
    background:
      radial-gradient(circle at 560px 330px, rgba(255,255,255,.75) 0 150px, transparent 260px),
      radial-gradient(circle at 120px 380px, rgba(247,206,214,.45), transparent 240px),
      radial-gradient(circle at 620px 760px, rgba(247,206,214,.5), transparent 260px),
      radial-gradient(circle at 60px 800px, rgba(247,206,214,.5), transparent 200px),
      var(--blush-pale);
  }
  .top-strip { position: absolute; left: 0; top: 9px; width: 1200px; height: 10px; background: var(--blush-strip); opacity: .6; z-index: 2; }
  .bottom-strip { position: absolute; left: 0; bottom: 0; width: 1200px; height: 20px; background: var(--blush-strip); opacity: .7; }

  /* Price list panel */
  .price-list { position: absolute; left: 80px; top: 98px; width: 292px; }
  .section { margin-bottom: 20px; }
  .section-title {
    font-size: 12.5px; font-weight: 700; letter-spacing: 1.6px; color: var(--slate);
    line-height: 20px; text-transform: uppercase;
  }
  .section-title small { display: block; font-size: 9px; letter-spacing: 1px; line-height: 12px; }
  .section-rule { border: 0; border-top: 1px solid var(--rule); margin: 3px 0 14px; }
  .price-table { display: grid; grid-template-columns: 214px 1fr; position: relative; }
  .price-table::after {
    content: ""; position: absolute; left: 214px; top: -4px; bottom: -4px;
    border-left: 1.5px dotted #8a8f99;
  }
  .price-table span { font-size: 11.5px; font-weight: 300; line-height: 19px; white-space: nowrap; }
  .price-table .price { padding-left: 28px; }
  .note { font-size: 11.5px; font-weight: 300; line-height: 15px; }
  .note i { font-style: italic; }
  .offer { font-size: 11.5px; font-weight: 300; line-height: 20px; }

  /* Contact panel */
  .contact-logo { position: absolute; left: 486px; top: 478px; color: var(--slate); font-weight: 300; }
  .logo-name { display: block; font-size: 44px; letter-spacing: 2px; line-height: 44px; }
  .logo-sub { display: block; font-size: 8px; letter-spacing: 5px; margin: 6px 0 0 16px; }
  .address { position: absolute; left: 498px; top: 574px; font-size: 11.5px; font-weight: 300; line-height: 16px; font-style: normal; }
  .phone { position: absolute; left: 498px; top: 630px; font-size: 16px; font-weight: 700; color: var(--slate); letter-spacing: .5px; }

  /* Cover panel */
  .cover-photo {
    position: absolute; left: 780px; top: 250px; width: 420px; height: 578px;
    background:
      radial-gradient(ellipse at 260px 250px, #ead2c6 0 120px, transparent 230px),
      radial-gradient(ellipse at 380px 120px, #d8bf96, transparent 200px),
      linear-gradient(160deg, #f6e9e4, #e9cfc4 60%, #f3e3de);
  }
  .cover-header {
    position: absolute; left: 816px; top: 0; width: 384px; height: 250px;
    background: var(--slate); border-bottom-left-radius: 30px;
    color: var(--white); font-weight: 300; padding: 118px 0 0 80px;
  }
  .cover-header .logo-name { font-size: 56px; line-height: 56px; }
  .cover-header .logo-sub { font-size: 10px; letter-spacing: 8px; margin: 12px 0 0 36px; }

  .footer-band {
    position: absolute; left: 391px; top: 686px; width: 789px; height: 142px;
    background: var(--band-grey); opacity: .95; border-top-right-radius: 30px; color: var(--white);
  }
  .social { position: absolute; left: 62px; top: 32px; }
  .social-row { display: flex; align-items: center; gap: 14px; height: 34px; font-size: 11.5px; }
  .social-mark { width: 22px; height: 22px; border: 2px solid var(--blush); border-radius: 5px; }
  .web { font-size: 17px; letter-spacing: .5px; }
  .web-contact { position: absolute; left: 106px; top: 98px; }
  .web-cover { position: absolute; left: 510px; top: 98px; }
</style>
</head>
<body>
<main class="brochure">
  <div class="top-strip"></div>

  <section class="price-list">
    <div class="section">
      <h2 class="section-title">Chemical Peels<br>Clarion Dr Peels 30min</h2>
      <hr class="section-rule">
      <div class="price-table">
        <span>Lactic Acid Peels 20%/40%/60%</span><span class="price">$120</span>
        <span>Youth Restore Peel</span><span class="price">$120</span>
        <span>Even Tone Pigment Peel</span><span class="price">$120</span>
        <span>Clear Skin Peel</span><span class="price">$120</span>
      </div>
    </div>
    <div class="section">
      <h2 class="section-title">Veridel Peels &nbsp;30min</h2>
      <hr class="section-rule">
      <div class="price-table">
        <span>Wild Berry Peel</span><span class="price">$120</span>
        <span>Red Citrus Peel</span><span class="price">$120</span>
        <span>Balance Peel</span><span class="price">$120</span>
        <span>Ageless Vitamin A Peel</span><span class="price">$250</span>
      </div>
    </div>
    <div class="section">
      <h2 class="section-title">Lumatone LED</h2>
      <hr class="section-rule">
      <p class="note">$90 per treatment <i>or</i><br>$50 when added on to any<br>of our other skin treatments.</p>
    </div>
    <div class="section">
      <h2 class="section-title">Micropoint Microneedling<small>(Collagen Induction Therapy)</small></h2>
      <hr class="section-rule">
      <p class="offer">$350 full face<br>$450 face, neck and décolletage</p>
    </div>
    <div class="section">
      <h2 class="section-title">Solavex Laser Facial</h2>
      <hr class="section-rule">
      <p class="offer">$350 full face<br>$450 face, neck and décolletage</p>
    </div>
  </section>

  <div class="contact-logo">
    <span class="logo-name">willow</span>
    <span class="logo-sub">AESTHETICS</span>
  </div>
  <address class="address">4/27 Harbour Road<br>Brookvale Ridge<br>Western Australia</address>
  <p class="phone">(08) 9123 4567</p>

  <div class="cover-photo" role="img" aria-label="Portrait photograph of a woman with fair skin and blonde hair, hands resting on her face"></div>

  <header class="cover-header">
    <span class="logo-name">willow</span>
    <span class="logo-sub">AESTHETICS</span>
  </header>

  <footer class="footer-band">
    <div class="social">
      <div class="social-row"><span class="social-mark"></span><span>willow_aesthetics</span></div>
      <div class="social-row"><span class="social-mark"></span><span>@willowaestheticsaustralia</span></div>
    </div>
    <p class="web web-contact">willowaesthetics.com.au</p>
    <p class="web web-cover">willowaesthetics.com.au</p>
  </footer>

  <div class="bottom-strip"></div>
</main>
</body>
</html>
```